LKT business card design

Coastal Guard Auxiliary Kin Services exists to provide timely and relevant programs and services to assist commanders with their role to ensure their assigned Families (Soldiers, spouses, children, significant others) have the highest possible level of well-being, and are the "ready" (for deployment, family separation, and self-sufficiency during that separation). We accomplish this task through several functional areas: Leadership (Director), Coordination (Coordinator--coordinates a variety of human services, staff sections, sister agencies, etc. to offer training and support), unit Family Readiness Programs, Junior Learner and Campus Aid, Bereaved Contact Network, Lantern Path Initiative (deployment and reintegration training), Recovery Care (for wounded warriors), Crisis Intervention, and Prevention Education and Training. Our aim is to demonstrate "Kin Above All" in everything we do, because Family Readiness improves Soldier Readiness which improves Army Readiness.

Folks, I've tried to upload the logos I mentioned, with not luck. You can get a look at one version of the Guard Auxiliary Kin Services logo at www.gaks-example.org.

Reason: Extendinig a couple days because I've not yet had any sucess uploading logos I mention in the brief. Hoping to crack the nut on that soon Thanks for your patient work.

Target Market(s)

Army Reserve Commanders, First Sergeants, Adult & Youth Volunteers & Family Members who are called to contribute to Whole Guard Kin readiness by being skilled at handling the challendes of deployment, family separation, and the self-sufficiency required when their Soldier deploys (e.g., fulfilling the Soldiers roles on the homefront while he or she is away)

Industry/Entity Type

Training

Contact Information for Business Card

Dr. Marcus T. Holloway, Director
Family Programs, 4th RDG, CGAWEST
2846 Ridge Lane
Honolulu, HI 96502-4718
808-555-0172 ext. 4820
BB: 808-555-0639
marcus.t.holloway7.staff@postbox-example.net

Requirements
Must have
• Family Programs Logo with text
Nice to have
• 4th RDG and CGAWEST Logo
Should not have
• old GAKS Logo (Green, blue globe with family silhouette)

```html
<!DOCTYPE html>
<html lang="en">
<head>
<meta charset="utf-8">
<title>LKT Business Card</title>
<link rel="stylesheet" href="https://fonts.googleapis.com/css2?family=Outfit:wght@700&family=Tinos:wght@400;700&display=swap">
<style>
  :root {
    --paper: #ffffff;
    --ink: #000000;
    --brand-navy: #0e1a3c;
    --badge-blue: #1034a6;
    --serif: "Tinos", "Times New Roman", serif;
    --brand-sans: "Outfit", "Helvetica Neue", Arial, sans-serif;
  }
  html, body {
    margin: 0;
    padding: 0;
    width: 1200px;
    height: 702px;
    overflow: hidden;
    background: var(--paper);
  }
  .card {
    position: relative;
    width: 1200px;
    height: 702px;
    background: var(--paper);
    color: var(--ink);
    font-family: var(--serif);
  }
  .brand {
    position: absolute;
    left: 100px;
    top: 128px;
    display: flex;
    align-items: center;
    gap: 24px;
  }
  .brand-dot {
    width: 118px;
    height: 118px;
    border-radius: 50%;
    background: var(--brand-navy);
    flex: none;
  }
  .brand-name {
    font-family: var(--brand-sans);
    font-weight: 700;
    font-size: 31px;
    line-height: 1.12;
    color: var(--brand-navy);
    text-transform: uppercase;
    letter-spacing: 0.2px;
  }
  .unit-badge {
    position: absolute;
    left: 692px;
    top: 176px;
    width: 90px;
    height: 90px;
    border-radius: 50%;
    background: var(--badge-blue);
  }
  .person {
    position: absolute;
    left: 130px;
    top: 330px;
  }
  .person-name {
    margin: 0 0 14px;
    font-size: 36px;
    font-weight: 700;
    line-height: 1;
  }
  .person-role {
    margin: 0;
    font-size: 24px;
    line-height: 40px;
  }
  .contact {
    position: absolute;
    left: 698px;
    top: 336px;
    font-size: 29px;
    line-height: 1;
  }
  .contact-address {
    margin: 0 0 22px;
  }
  .contact-row {
    display: flex;
    align-items: flex-start;
    gap: 18px;
    margin-bottom: 14px;
  }
  .contact-icon {
    width: 34px;
    height: 34px;
    flex: none;
  }
  .contact-lines {
    line-height: 34px;
  }
  .contact-email {
    font-size: 24px;
  }
</style>
</head>
<body>
  <div class="card">
    <div class="brand">
      <div class="brand-dot"></div>
      <div class="brand-name">Guard Auxiliary<br>Kin Services</div>
    </div>

    <div class="unit-badge"></div>

    <div class="person">
      <h1 class="person-name">Dr. Marcus T. Holloway</h1>
      <p class="person-role">Director Family Programs</p>
      <p class="person-role">4th RDG, CGAWEST</p>
    </div>

    <div class="contact">
      <p class="contact-address">2846 Ridge Lane Honolulu, HI</p>

      <div class="contact-row">
        <svg class="contact-icon" viewBox="0 0 34 34" aria-hidden="true">
          <rect width="34" height="34" rx="7" fill="#000"/>
          <path d="M11 8c1.5-.6 2.4 0 3 1.3l1.3 3c.4 1-.1 1.8-.9 2.3l-1 .7c.9 2 2.3 3.6 4.2 4.6l.8-1c.6-.8 1.4-1.1 2.3-.7l3 1.4c1.2.6 1.6 1.6 1 3-.8 1.8-2.7 2.7-4.6 2.2C14.6 23.5 10 19 8.7 13c-.5-2.1.5-4.2 2.3-5z" fill="#fff"/>
        </svg>
        <div class="contact-lines">96502-4718<br>808-555-0172 ext. 4820</div>
      </div>

      <div class="contact-row">
        <svg class="contact-icon" viewBox="0 0 34 34" aria-hidden="true">
          <rect width="34" height="34" rx="7" fill="#000"/>
          <rect x="11" y="6" width="12" height="22" rx="2.5" fill="none" stroke="#fff" stroke-width="2"/>
          <circle cx="17" cy="24" r="1.4" fill="#fff"/>
        </svg>
        <div class="contact-lines">808-555-0639</div>
      </div>

      <div class="contact-row">
        <svg class="contact-icon" viewBox="0 0 34 34" aria-hidden="true">
          <rect width="34" height="34" rx="7" fill="#000"/>
          <text x="17" y="24" text-anchor="middle" font-family="Tinos, serif" font-size="21" fill="#fff">@</text>
        </svg>
        <div class="contact-lines contact-email">marcus.t.holloway7.staff@postbox-example.net</div>
      </div>
    </div>
  </div>
</body>
</html>
```